Summer Music/Chorus/Choir Camp for Young Singers Ages 8-13

We need a flyer for a summer camp for young singers ages 8-13. We are nonprofit community children's chorus in Miami, FL. Our camp provides specialized training in music theory, sight-reading,and aural training through daily choral rehearsals in an environment that is both positive and a lot of fun! Our camp offers children the opportunity to come as they are, no matter the level of experience, and grow tremendously in their musicianship skills. In addition to this, our campers participate in song-writing, masterclasses, community performances, and media projects. The final design should be clean, fun, not too crowded, should appeal to boys and girls ages 8-13, and something someone that age would consider "cool" and not too childish. Drawings are cool, something different.
Updates

Target Market(s)

Ages 8-13 and parents of those kids.

Industry/Entity Type

Community

Requirements
Must have
• All info attached.
Nice to have
• Things that relate to music, especially related to singing/choirs
Should not have
• instruments, stock photos of children, or photos from our website (unless they are used very creatively), or photos in general. I've attached our previous camp flyer and our current organization flyer but I don't necessarily want this flyer to look like those.

```html
<!DOCTYPE html>
<html lang="en">
<head>
<meta charset="utf-8">
<title>Bright Notes Chorus – Summer Choral Camp</title>
<link rel="stylesheet" href="https://fonts.googleapis.com/css2?family=Cherry+Swash:wght@700&family=Fjalla+One&family=Source+Sans+3:wght@400;600;700&family=Roboto+Condensed:wght@400&display=swap">
<style>
  :root {
    --stage: #3a3a3c;
    --paper: #ffffff;
    --paper-shade: #ececec;
    --pink: #e3167f;
    --teal: #1d8a97;
    --teal-dark: #2f7f7b;
    --green: #23a37c;
    --blue: #1b8fc0;
    --ink: #222222;
    --badge: #2a2a2a;
    --badge-purple: #8b3fa8;
    --art-teal: #5fcfb9;
    --art-pink: #f59acb;
    --art-yellow: #ffe07a;
    --art-blue: #8fcdf2;
  }
  * { box-sizing: border-box; margin: 0; padding: 0; }
  html, body { width: 1200px; height: 1200px; overflow: hidden; }
  body { background: var(--stage); position: relative; }

  .flyer {
    position: absolute; left: 195px; top: 30px;
    width: 810px; height: 1140px;
    background: radial-gradient(ellipse at 55% 40%, var(--paper) 0%, var(--paper) 45%, var(--paper-shade) 100%);
    font-family: "Source Sans 3", sans-serif;
    overflow: hidden;
  }

  .brand { position: absolute; left: 63px; top: 58px; display: flex; align-items: center; gap: 14px; }
  .brand-dot { width: 34px; height: 34px; border-radius: 50%; background: var(--teal-dark); }
  .brand-name {
    font-family: "Source Sans 3", sans-serif; font-weight: 600;
    color: var(--teal-dark); font-size: 44px; line-height: 1.0;
  }

  .dates { position: absolute; right: 23px; top: 40px; text-align: right; }
  .dates-days { font-family: "Fjalla One", sans-serif; color: var(--teal); font-size: 52px; line-height: 1.05; }
  .dates-hours { font-family: "Fjalla One", sans-serif; color: var(--green); font-size: 28px; line-height: 1.1; }

  .invite {
    position: absolute; right: 52px; top: 163px; text-align: right;
    font-family: "Fjalla One", sans-serif; color: var(--blue);
    font-size: 24px; line-height: 1.2;
  }

  .title {
    position: absolute; left: 60px; top: 248px;
    font-family: "Cherry Swash", serif; font-weight: 700;
    color: var(--pink); font-size: 56px; line-height: 1.05;
  }

  .pricing { position: absolute; right: 52px; top: 268px; text-align: right; font-family: "Fjalla One", sans-serif; }
  .pricing-cost { color: var(--pink); font-size: 36px; line-height: 1.15; }
  .pricing-session { color: var(--teal); font-size: 34px; line-height: 1.15; }
  .pricing-note { color: var(--teal); font-size: 15px; line-height: 1.3; }

  .music-art {
    position: absolute; left: 85px; top: 388px; width: 725px; height: 432px;
    border-radius: 28px 0 0 28px;
    background: linear-gradient(100deg,
      var(--art-teal) 0%, var(--art-teal) 16%,
      var(--art-pink) 42%, var(--art-yellow) 68%, var(--art-blue) 100%);
  }

  .info { position: absolute; left: 63px; top: 828px; }
  .info-label { font-weight: 700; color: var(--pink); font-size: 23px; line-height: 27px; letter-spacing: 0.5px; }
  .info-line { color: var(--blue); font-size: 21px; line-height: 27px; }
  .info-line--strong { font-weight: 700; }
  .info-block + .info-label { margin-top: 4px; }

  .sponsors { position: absolute; left: 603px; top: 905px; width: 160px; height: 135px; }
  .sponsor { position: absolute; background: var(--badge); }
  .sponsor--a { left: 0; top: 0; width: 50px; height: 50px; }
  .sponsor--b { left: 0; top: 78px; width: 50px; height: 26px; }
  .sponsor--c { left: 0; top: 116px; width: 100px; height: 16px; }
  .sponsor--d { left: 95px; top: 38px; width: 55px; height: 55px; background: var(--badge-purple); }
  .access { position: absolute; top: 4px; width: 22px; height: 22px; border-radius: 50%; background: var(--badge); }
  .access--a { left: 92px; }
  .access--b { left: 124px; }

  .nonprofit {
    position: absolute; left: 0; right: 0; top: 1064px; text-align: center;
    font-size: 13.5px; line-height: 18px; color: var(--ink);
  }
  .fineprint {
    position: absolute; left: 28px; right: 28px; top: 1088px; text-align: center;
    font-family: "Roboto Condensed", sans-serif; text-transform: uppercase;
    font-size: 8.4px; line-height: 1.3; color: #444444;
  }
</style>
</head>
<body>
  <main class="flyer">
    <div class="brand">
      <span class="brand-dot"></span>
      <span class="brand-name">Bright Notes<br>Chorus</span>
    </div>

    <div class="dates">
      <p class="dates-days">July 18-29</p>
      <p class="dates-hours">9am-3pm (M-F)</p>
    </div>

    <p class="invite">Calling All Boys And Girls<br>In Grades 3 Through 9<br>Who Love To Sing!</p>

    <h1 class="title">Summer<br>Choral Camp</h1>

    <div class="pricing">
      <p class="pricing-cost">COST- *$300</p>
      <p class="pricing-session">FOR 2-WEEK SESSION</p>
      <p class="pricing-note">*PRICE DOES NOT INCLUDE LUNCH</p>
    </div>

    <div class="music-art" role="img" aria-label="Illustration of a large teal treble clef with a flowing musical staff full of colourful notes"></div>

    <div class="info">
      <p class="info-label">LOCATION</p>
      <div class="info-block">
        <p class="info-line">Palm Grove Community Arts Hall</p>
        <p class="info-line">4820 Coral Tree Avenue</p>
        <p class="info-line">Miami, FL 33199</p>
      </div>
      <p class="info-label">CONTACT</p>
      <div class="info-block">
        <p class="info-line info-line--strong">555.014.2368</p>
        <p class="info-line info-line--strong">hello@brightnoteschorus.org</p>
        <p class="info-line">www.brightnoteschorus.org</p>
      </div>
    </div>

    <div class="sponsors" aria-label="Partner badges">
      <span class="sponsor sponsor--a"></span>
      <span class="access access--a"></span>
      <span class="access access--b"></span>
      <span class="sponsor sponsor--d"></span>
      <span class="sponsor sponsor--b"></span>
      <span class="sponsor sponsor--c"></span>
    </div>

    <p class="nonprofit">Bright Notes Chorus is a 501 (c)(3) nonprofit organization. Donations made to BNC are tax-exempt.</p>
    <p class="fineprint">Our facility meets all accessibility requirements. Assistive listening devices are available in the main auditorium and the studio theater. To request materials in an accessible format or any other accommodation to attend an event, please contact our front office at least five days in advance. Relay users may call 711. Requests can be made by phone or email, and staff will respond within two business days to confirm arrangements.</p>
  </main>
</body>
</html>
```